Kivo Commercial Cleaning is lookong for a new business card design.

A fresh new design that's professional and stylish. We need a serious upgrade to our business cards. I have included pictures of our existing ones. Our clients include professional individuals and business owners. We woupdblike something professional and upbeat. Please have fun and see what you come uo with.

Target Market(s)

Property managers, business owners, facility managers and other similar professionals

Industry/Entity Type

Janitorial

Contact Information for Business Card

Name, cell, office number, email, web address

Font styles to use
Sans Serif

Colors

Designer to choose colors to be used in the design.

Requirements
Must have
• please use the green color in our logo
Nice to have
• Bar code
Should not have
• Address

```html
<!DOCTYPE html>
<html lang="en">
<head>
<meta charset="utf-8">
<title>Kivo Commercial Cleaning — Business Card</title>
<link href="https://fonts.googleapis.com/css2?family=Rubik:wght@400;500;700;800&display=swap" rel="stylesheet">
<style>
  :root {
    --green: #47ff2a;
    --white: #ffffff;
    --backdrop: #d9d9d9;
    --shadow: rgba(0, 0, 0, 0.22);
  }
  * { box-sizing: border-box; margin: 0; padding: 0; }
  html, body { width: 1200px; height: 846px; overflow: hidden; }
  body {
    background: var(--backdrop);
    font-family: "Rubik", Arial, sans-serif;
    position: relative;
  }
  .card {
    position: absolute;
    left: 346px;
    width: 508px;
    height: 290px;
    background: var(--white);
    box-shadow: 12px 12px 14px var(--shadow);
    overflow: hidden;
  }
  .card--front { top: 99px; }
  .card--back { top: 456px; }

  /* Front */
  .wordmark {
    position: absolute;
    color: var(--green);
    font-weight: 700;
    letter-spacing: -2px;
    line-height: 1;
  }
  .card--front .wordmark { left: 36px; top: 62px; font-size: 86px; }
  .contact-list { position: absolute; left: 246px; top: 76px; list-style: none; }
  .contact-item {
    display: flex; align-items: center; height: 25px; margin-bottom: 5.5px;
    color: var(--green); font-size: 18.5px; font-weight: 400; letter-spacing: 0.2px;
  }
  .contact-icon {
    width: 25px; height: 25px; border-radius: 50%; background: var(--green);
    margin-right: 7px; flex: none; display: flex; align-items: center; justify-content: center;
  }
  .rule { position: absolute; left: 0; width: 100%; background: var(--green); }
  .rule--thin { top: 220px; height: 2px; }
  .rule--mid { top: 226px; height: 5px; }
  .name-band {
    position: absolute; left: 0; top: 235px; width: 100%; height: 55px;
    background: var(--green); display: flex; align-items: center; justify-content: flex-end;
    padding-right: 38px;
  }
  .name { color: var(--white); font-size: 24px; font-weight: 700; letter-spacing: 0.2px; }

  /* Back */
  .brand-panel {
    position: absolute; left: 0; top: 0; width: 100%; height: 158px; background: var(--green);
  }
  .card--back .wordmark {
    color: var(--white); left: 0; width: 100%; text-align: center; top: 36px; font-size: 88px;
  }
  .tagline {
    position: absolute; left: 0; width: 100%; top: 119px; text-align: center;
    color: var(--white); font-size: 13px; font-weight: 500; letter-spacing: 0.4px;
  }
  .service-heading {
    position: absolute; top: 174px; left: 37px; right: 37px;
    display: flex; align-items: center; gap: 6px;
  }
  .service-heading::before, .service-heading::after {
    content: ""; flex: 1; height: 1px; background: var(--green);
  }
  .service-heading h2 {
    color: var(--green); font-size: 21.5px; font-weight: 800; letter-spacing: 0.2px; line-height: 26px;
  }
  .service-list { list-style: none; }
  .service {
    position: absolute; top: 212px; width: 80px; margin-left: -40px; text-align: center;
    color: var(--green); font-size: 11px; line-height: 13px; letter-spacing: 0.1px;
  }
  .service-icon {
    width: 34px; height: 34px; border-radius: 50%; background: var(--green);
    margin: 0 auto 8px; display: flex; align-items: center; justify-content: center;
  }
  svg { display: block; }
</style>
</head>
<body>

<section class="card card--front" aria-label="Business card front">
  <div class="wordmark">kivo</div>
  <ul class="contact-list">
    <li class="contact-item">
      <span class="contact-icon"><svg width="15" height="15" viewBox="0 0 24 24" fill="none" stroke="#fff" stroke-width="2" stroke-linecap="round" stroke-linejoin="round"><path d="M22 16.9v3a2 2 0 0 1-2.2 2 19.8 19.8 0 0 1-8.6-3.1 19.5 19.5 0 0 1-6-6A19.8 19.8 0 0 1 2.1 4.2 2 2 0 0 1 4.1 2h3a2 2 0 0 1 2 1.7c.1.9.4 1.8.7 2.7a2 2 0 0 1-.5 2.1L8 9.8a16 16 0 0 0 6 6l1.3-1.3a2 2 0 0 1 2.1-.4c.9.3 1.8.6 2.7.7a2 2 0 0 1 1.7 2z"/><path d="M15 5a5 5 0 0 1 4 4M15 1a9 9 0 0 1 8 8"/></svg></span>
      (555) 014-2739
    </li>
    <li class="contact-item">
      <span class="contact-icon"><svg width="14" height="14" viewBox="0 0 24 24" fill="none" stroke="#fff" stroke-width="2.2" stroke-linecap="round"><rect x="6" y="2" width="12" height="20" rx="2"/><path d="M11 18h2"/></svg></span>
      800-555-0146
    </li>
    <li class="contact-item">
      <span class="contact-icon"><svg width="15" height="15" viewBox="0 0 24 24" fill="none" stroke="#fff" stroke-width="2" stroke-linejoin="round"><rect x="2" y="5" width="20" height="14" rx="1"/><path d="M2 6l10 7 10-7M2 18l7-6M22 18l-7-6"/></svg></span>
      marco@kivocleaning.com
    </li>
    <li class="contact-item">
      <span class="contact-icon"><svg width="15" height="15" viewBox="0 0 24 24" fill="none" stroke="#fff" stroke-width="1.8"><circle cx="12" cy="12" r="10"/><path d="M2 12h20M12 2c3 3 3 17 0 20M12 2c-3 3-3 17 0 20"/></svg></span>
      www.kivocleaning.com
    </li>
  </ul>
  <div class="rule rule--thin"></div>
  <div class="rule rule--mid"></div>
  <div class="name-band"><p class="name">Marco Delgado</p></div>
</section>

<section class="card card--back" aria-label="Business card back">
  <div class="brand-panel">
    <div class="wordmark">kivo</div>
    <p class="tagline">kivo commercial cleaning</p>
  </div>
  <div class="service-heading"><h2>WHO WE SERVICE</h2></div>
  <ul class="service-list">
    <li class="service" style="left:62px">
      <span class="service-icon"><svg width="20" height="20" viewBox="0 0 24 24" fill="none" stroke="#fff" stroke-width="1.8" stroke-linejoin="round"><path d="M12 21l-8-8a5 5 0 0 1 8-6 5 5 0 0 1 8 6z"/><path d="M4 12h4l2-4 3 7 2-3h5"/></svg></span>
      MEDICAL
    </li>
    <li class="service" style="left:137px">
      <span class="service-icon"><svg width="20" height="20" viewBox="0 0 24 24" fill="none" stroke="#fff" stroke-width="1.6"><path d="M3 21h18M5 21v-8h5v8M10 21V8l8-4v17"/><path d="M13 9h2M13 12h2M13 15h2M7 16h1"/></svg></span>
      OFFICE<br>BUILDINGS
    </li>
    <li class="service" style="left:213px">
      <span class="service-icon"><svg width="20" height="20" viewBox="0 0 24 24" fill="none" stroke="#fff" stroke-width="1.6" stroke-linejoin="round"><rect x="5" y="4" width="14" height="18" rx="1"/><rect x="9" y="2" width="6" height="4"/><path d="M8 15l2-4 2 5 2-3 2 2"/></svg></span>
      HEALTH<br>CARE
    </li>
    <li class="service" style="left:289px">
      <span class="service-icon"><svg width="20" height="20" viewBox="0 0 24 24" fill="none" stroke="#fff" stroke-width="1.8" stroke-linecap="round"><path d="M14.7 6.3a4 4 0 0 0-5.4-5l2.5 2.5-1.4 1.4-2.5-2.5a4 4 0 0 0 5 5.4L19 14"/><circle cx="20" cy="17" r="2"/></svg></span>
      INDUSTRIAL
    </li>
    <li class="service" style="left:365px">
      <span class="service-icon"><svg width="20" height="20" viewBox="0 0 24 24" fill="none" stroke="#fff" stroke-width="1.6" stroke-linejoin="round"><path d="M4 4h16l2 5H2z"/><path d="M4 9v12h16V9M7 21v-7h4v7M13 14h4v3h-4z"/></svg></span>
      RETAIL
    </li>
    <li class="service" style="left:442px">
      <span class="service-icon"><svg width="20" height="20" viewBox="0 0 24 24" fill="none" stroke="#fff" stroke-width="1.7" stroke-linejoin="round"><path d="M2 5h7a3 3 0 0 1 3 3v12a2 2 0 0 0-2-2H2zM22 5h-7a3 3 0 0 0-3 3v12a2 2 0 0 1 2-2h8z"/></svg></span>
      PLACES OF<br>WORSHIP
    </li>
  </ul>
</section>

</body>
</html>
```